Innovative Freezer Label Design

Create a versatile and innovative freezer label design with universal appeal, suitable for different functionalities. The design should cater to a diverse audience, including those who freeze meals for meal prepping, batch cooking, and the restaurant industry. Our vision is a visually striking and distinctive design that embodies simplicity.

Example "our current labels feature essential details like "Contents" and "Date." We recognize these as crucial points of information. Currently, the challenge lies in creating various labels for different marketplaces, considering language barriers. A proposed solution involves the integration of universal icons to replace specific words, promoting practicality for international sales."

Kindly note that design concepts should not be restricted to our current product, brand guideline, logo, or the provided example.

Our goal is not only product differentiation but also increased sales through a blend of functionality and aesthetics.

The following are examples of freezer labels designs. Kindly do not restrict your designs to the examples. The designs must be universal (for language barrier purposes)

Examples:
https://www.snaprovel.co.uk/pin/5820174630298837415/
https://www.snaprovel.co.uk/pin/5820174630298837419/
https://www.snaprovel.co.uk/pin/5820174630298837408/
https://www.snaprovel.co.uk/pin/5820174630298837322/
https://www.snaprovel.co.uk/pin/5820174630298898764/

Please reach out if you have any questions.

Thank you

```html
<!DOCTYPE html>
<html lang="en">
<head>
<meta charset="utf-8">
<title>Freezer Label Collection</title>
<link rel="stylesheet" href="https://fonts.googleapis.com/css2?family=Inter:wght@400&display=swap">
<style>
  :root {
    --page: #fdf4ea;
    --edge: #3e4b56;
    --cream: #fbfaf6;
    --tan: #e6cb9b;
    --peach: #f9cbb0;
    --salmon: #f3918b;
    --silver: #c5c6ca;
    --mustard: #d6a941;
    --mint: #9ed293;
    --navy: #37495a;
    --steel: #4d759d;
    --graphite: #6b6b6b;
    --olive: #5a5b3b;
    --khaki: #6a5f45;
    --cocoa: #4f2d15;
    --charcoal: #26282a;
    --ink-dark: #4a3a30;
    --ink-light: #f4ece2;
  }
  * { box-sizing: border-box; margin: 0; padding: 0; }
  html, body { width: 1200px; height: 1110px; overflow: hidden; background: var(--page); }
  .sprite { position: absolute; width: 0; height: 0; }
  .sheet {
    position: absolute; top: 60px;
    display: grid;
    grid-template-columns: 258px 258px;
    grid-auto-rows: 128px;
    column-gap: 18px; row-gap: 16px;
  }
  .sheet--light { left: 46px; }
  .sheet--dark { left: 619px; }
  .label {
    position: relative;
    background: var(--bg);
    border: 2px solid var(--edge);
    box-shadow: 0 2px 4px rgba(0,0,0,.18);
    --icon-line: var(--ink-dark);
    --rule: #8c8c8c;
    --mark: #4a4a4a;
  }
  .label:nth-child(odd) { border-radius: 8px; }
  .label--dark { --icon-line: var(--ink-light); --rule: #aab0b5; --mark: #f1f1f1; border-color: #4a5560; }
  .food-row { position: absolute; left: 0; top: 6px; width: 254px; height: 36px; }
  .icon-note { position: absolute; left: 24px; top: 52px; width: 24px; height: 24px; }
  .rule { position: absolute; left: 24px; right: 26px; top: 86px; height: 1px; background: var(--rule); }
  .icon-cal { position: absolute; left: 27px; top: 98px; width: 24px; height: 22px; }
  .date {
    position: absolute; top: 99px; left: 104px;
    font: 400 16px/1 "Inter", sans-serif; color: var(--mark);
    display: flex; gap: 50px;
  }
  .brand {
    position: absolute; right: 10px; bottom: 7px;
    font: 400 10px/1 "Inter", sans-serif; color: var(--mark);
    letter-spacing: .3px;
  }
  .cream { --bg: var(--cream); } .tan { --bg: var(--tan); } .peach { --bg: var(--peach); }
  .salmon { --bg: var(--salmon); } .silver { --bg: var(--silver); } .mustard { --bg: var(--mustard); }
  .mint { --bg: var(--mint); } .navy { --bg: var(--navy); } .steel { --bg: var(--steel); }
  .graphite { --bg: var(--graphite); } .olive { --bg: var(--olive); } .khaki { --bg: var(--khaki); }
  .cocoa { --bg: var(--cocoa); } .charcoal { --bg: var(--charcoal); }
</style>
</head>
<body>
<svg class="sprite" aria-hidden="true">
  <defs>
    <symbol id="food-row" viewBox="0 0 254 36">
      <g stroke="var(--icon-line)" stroke-width="1.4" stroke-linejoin="round">
        <path d="M14 6 L20 14 L12 30 Z" fill="#f08a2c"/>
        <path d="M15 7 L12 1 M16 6 L20 2" fill="none" stroke="#5aa640" stroke-width="2"/>
        <circle cx="26" cy="22" r="8" fill="#e8403a"/>
        <path d="M23 14 L26 17 L29 14" fill="none" stroke="#5aa640" stroke-width="1.6"/>
        <path d="M70 12 C76 10 79 18 76 26 C74 30 68 30 67 26 C64 20 66 13 70 12 Z" fill="#a6c84a"/>
        <circle cx="62" cy="22" r="8" fill="#d9302b"/>
        <path d="M62 14 L63 9" fill="none"/>
        <ellipse cx="107" cy="22" rx="11" ry="7" fill="#8a4a22"/>
        <path d="M95 28 H121" fill="none" stroke-width="2"/>
        <path d="M114 15 L119 9" fill="none" stroke-width="2"/>
        <path d="M139 18 C140 11 156 10 159 17 C162 24 152 30 144 28 C138 26 138 22 139 18 Z" fill="#d45a63"/>
        <ellipse cx="150" cy="20" rx="4" ry="3" fill="#f6d9d6"/>
        <path d="M180 20 C186 11 200 11 206 20 C200 29 186 29 180 20 Z" fill="#f49a2a"/>
        <path d="M206 20 L214 13 L214 27 Z" fill="#f49a2a"/>
        <circle cx="186" cy="19" r="1.3" fill="var(--icon-line)"/>
        <path d="M227 22 C227 14 243 14 243 22 Z" fill="#e24b4b"/>
        <path d="M228 22 H242 L239 31 H231 Z" fill="#f2a2a8"/>
        <circle cx="235" cy="12" r="2" fill="#d9302b"/>
      </g>
    </symbol>
    <symbol id="icon-note" viewBox="0 0 24 24">
      <g fill="none" stroke="var(--icon-line)" stroke-width="1.4">
        <rect x="5" y="3" width="15" height="19" rx="1"/>
        <path d="M8 2 V5 M12 2 V5 M16 2 V5 M9 10 H17 M9 14 H17 M9 18 H15"/>
        <path d="M1 6 L6 15"/>
      </g>
    </symbol>
    <symbol id="icon-cal" viewBox="0 0 24 22">
      <g fill="none" stroke="var(--icon-line)" stroke-width="1.4">
        <rect x="1" y="3" width="18" height="15" rx="1"/>
        <path d="M1 7 H19 M5 1 V4 M15 1 V4"/>
        <path d="M4 10 H6 M8 10 H10 M12 10 H14 M4 14 H6 M8 14 H10" stroke-width="2"/>
        <circle cx="18" cy="17" r="4.5" fill="var(--bg)"/>
        <path d="M18 15 V17 H20"/>
      </g>
    </symbol>
  </defs>
</svg>

<section class="sheet sheet--light">
  <article class="label cream"><svg class="food-row"><use href="#food-row"/></svg><svg class="icon-note"><use href="#icon-note"/></svg><span class="rule"></span><svg class="icon-cal"><use href="#icon-cal"/></svg><span class="date"><span>/</span><span>/</span></span><span class="brand">Kelto</span></article>
  <article class="label cream"><svg class="food-row"><use href="#food-row"/></svg><svg class="icon-note"><use href="#icon-note"/></svg><span class="rule"></span><svg class="icon-cal"><use href="#icon-cal"/></svg><span class="date"><span>/</span><span>/</span></span><span class="brand">Kelto</span></article>
  <article class="label tan"><svg class="food-row"><use href="#food-row"/></svg><svg class="icon-note"><use href="#icon-note"/></svg><span class="rule"></span><svg class="icon-cal"><use href="#icon-cal"/></svg><span class="date"><span>/</span><span>/</span></span><span class="brand">Kelto</span></article>
  <article class="label tan"><svg class="food-row"><use href="#food-row"/></svg><svg class="icon-note"><use href="#icon-note"/></svg><span class="rule"></span><svg class="icon-cal"><use href="#icon-cal"/></svg><span class="date"><span>/</span><span>/</span></span><span class="brand">Kelto</span></article>
  <article class="label peach"><svg class="food-row"><use href="#food-row"/></svg><svg class="icon-note"><use href="#icon-note"/></svg><span class="rule"></span><svg class="icon-cal"><use href="#icon-cal"/></svg><span class="date"><span>/</span><span>/</span></span><span class="brand">Kelto</span></article>
  <article class="label peach"><svg class="food-row"><use href="#food-row"/></svg><svg class="icon-note"><use href="#icon-note"/></svg><span class="rule"></span><svg class="icon-cal"><use href="#icon-cal"/></svg><span class="date"><span>/</span><span>/</span></span><span class="brand">Kelto</span></article>
  <article class="label salmon"><svg class="food-row"><use href="#food-row"/></svg><svg class="icon-note"><use href="#icon-note"/></svg><span class="rule"></span><svg class="icon-cal"><use href="#icon-cal"/></svg><span class="date"><span>/</span><span>/</span></span><span class="brand">Kelto</span></article>
  <article class="label salmon"><svg class="food-row"><use href="#food-row"/></svg><svg class="icon-note"><use href="#icon-note"/></svg><span class="rule"></span><svg class="icon-cal"><use href="#icon-cal"/></svg><span class="date"><span>/</span><span>/</span></span><span class="brand">Kelto</span></article>
  <article class="label silver"><svg class="food-row"><use href="#food-row"/></svg><svg class="icon-note"><use href="#icon-note"/></svg><span class="rule"></span><svg class="icon-cal"><use href="#icon-cal"/></svg><span class="date"><span>/</span><span>/</span></span><span class="brand">Kelto</span></article>
  <article class="label silver"><svg class="food-row"><use href="#food-row"/></svg><svg class="icon-note"><use href="#icon-note"/></svg><span class="rule"></span><svg class="icon-cal"><use href="#icon-cal"/></svg><span class="date"><span>/</span><span>/</span></span><span class="brand">Kelto</span></article>
  <article class="label mustard"><svg class="food-row"><use href="#food-row"/></svg><svg class="icon-note"><use href="#icon-note"/></svg><span class="rule"></span><svg class="icon-cal"><use href="#icon-cal"/></svg><span class="date"><span>/</span><span>/</span></span><span class="brand">Kelto</span></article>
  <article class="label mustard"><svg class="food-row"><use href="#food-row"/></svg><svg class="icon-note"><use href="#icon-note"/></svg><span class="rule"></span><svg class="icon-cal"><use href="#icon-cal"/></svg><span class="date"><span>/</span><span>/</span></span><span class="brand">Kelto</span></article>
  <article class="label mint"><svg class="food-row"><use href="#food-row"/></svg><svg class="icon-note"><use href="#icon-note"/></svg><span class="rule"></span><svg class="icon-cal"><use href="#icon-cal"/></svg><span class="date"><span>/</span><span>/</span></span><span class="brand">Kelto</span></article>
  <article class="label mint"><svg class="food-row"><use href="#food-row"/></svg><svg class="icon-note"><use href="#icon-note"/></svg><span class="rule"></span><svg class="icon-cal"><use href="#icon-cal"/></svg><span class="date"><span>/</span><span>/</span></span><span class="brand">Kelto</span></article>
</section>

<section class="sheet sheet--dark">
  <article class="label label--dark navy"><svg class="food-row"><use href="#food-row"/></svg><svg class="icon-note"><use href="#icon-note"/></svg><span class="rule"></span><svg class="icon-cal"><use href="#icon-cal"/></svg><span class="date"><span>/</span><span>/</span></span><span class="brand">Kelto</span></article>
  <article class="label label--dark navy"><svg class="food-row"><use href="#food-row"/></svg><svg class="icon-note"><use href="#icon-note"/></svg><span class="rule"></span><svg class="icon-cal"><use href="#icon-cal"/></svg><span class="date"><span>/</span><span>/</span></span><span class="brand">Kelto</span></article>
  <article class="label label--dark steel"><svg class="food-row"><use href="#food-row"/></svg><svg class="icon-note"><use href="#icon-note"/></svg><span class="rule"></span><svg class="icon-cal"><use href="#icon-cal"/></svg><span class="date"><span>/</span><span>/</span></span><span class="brand">Kelto</span></article>
  <article class="label label--dark steel"><svg class="food-row"><use href="#food-row"/></svg><svg class="icon-note"><use href="#icon-note"/></svg><span class="rule"></span><svg class="icon-cal"><use href="#icon-cal"/></svg><span class="date"><span>/</span><span>/</span></span><span class="brand">Kelto</span></article>
  <article class="label label--dark graphite"><svg class="food-row"><use href="#food-row"/></svg><svg class="icon-note"><use href="#icon-note"/></svg><span class="rule"></span><svg class="icon-cal"><use href="#icon-cal"/></svg><span class="date"><span>/</span><span>/</span></span><span class="brand">Kelto</span></article>
  <article class="label label--dark graphite"><svg class="food-row"><use href="#food-row"/></svg><svg class="icon-note"><use href="#icon-note"/></svg><span class="rule"></span><svg class="icon-cal"><use href="#icon-cal"/></svg><span class="date"><span>/</span><span>/</span></span><span class="brand">Kelto</span></article>
  <article class="label label--dark olive"><svg class="food-row"><use href="#food-row"/></svg><svg class="icon-note"><use href="#icon-note"/></svg><span class="rule"></span><svg class="icon-cal"><use href="#icon-cal"/></svg><span class="date"><span>/</span><span>/</span></span><span class="brand">Kelto</span></article>
  <article class="label label--dark olive"><svg class="food-row"><use href="#food-row"/></svg><svg class="icon-note"><use href="#icon-note"/></svg><span class="rule"></span><svg class="icon-cal"><use href="#icon-cal"/></svg><span class="date"><span>/</span><span>/</span></span><span class="brand">Kelto</span></article>
  <article class="label label--dark khaki"><svg class="food-row"><use href="#food-row"/></svg><svg class="icon-note"><use href="#icon-note"/></svg><span class="rule"></span><svg class="icon-cal"><use href="#icon-cal"/></svg><span class="date"><span>/</span><span>/</span></span><span class="brand">Kelto</span></article>
  <article class="label label--dark khaki"><svg class="food-row"><use href="#food-row"/></svg><svg class="icon-note"><use href="#icon-note"/></svg><span class="rule"></span><svg class="icon-cal"><use href="#icon-cal"/></svg><span class="date"><span>/</span><span>/</span></span><span class="brand">Kelto</span></article>
  <article class="label label--dark cocoa"><svg class="food-row"><use href="#food-row"/></svg><svg class="icon-note"><use href="#icon-note"/></svg><span class="rule"></span><svg class="icon-cal"><use href="#icon-cal"/></svg><span class="date"><span>/</span><span>/</span></span><span class="brand">Kelto</span></article>
  <article class="label label--dark cocoa"><svg class="food-row"><use href="#food-row"/></svg><svg class="icon-note"><use href="#icon-note"/></svg><span class="rule"></span><svg class="icon-cal"><use href="#icon-cal"/></svg><span class="date"><span>/</span><span>/</span></span><span class="brand">Kelto</span></article>
  <article class="label label--dark charcoal"><svg class="food-row"><use href="#food-row"/></svg><svg class="icon-note"><use href="#icon-note"/></svg><span class="rule"></span><svg class="icon-cal"><use href="#icon-cal"/></svg><span class="date"><span>/</span><span>/</span></span><span class="brand">Kelto</span></article>
  <article class="label label--dark charcoal"><svg class="food-row"><use href="#food-row"/></svg><svg class="icon-note"><use href="#icon-note"/></svg><span class="rule"></span><svg class="icon-cal"><use href="#icon-cal"/></svg><span class="date"><span>/</span><span>/</span></span><span class="brand">Kelto</span></article>
</section>
</body>
</html>
```